Business card design for Velvet Harbor

We need business cards designed for our new marketing consulting company, Velvet Harbor. Our services include marketing strategy, go-to-market and launch planning, growth strategy, and execution. We serve medical technology and health technology companies, from startups to well-established growth companies.

The business cards should feel professional, credible, reliable and trustworthy, and should instill confidence. Also bold, creative, and modern.

The design must use the Velvet Harbor logo.

The primary brand color is this orange: #FF5501
A secondary color that you can use is this gray: #282B2D
I would prefer only to use the orange and gray. But if you feel you really need an additional accent color (please use it very sparingly, as little as possible), you can use this blue for small accent purposes: #009FED

Attached are the logo files. The main logo is the one with a little bit of orange on the left and the rest is gray.

The business card should include the following:

Velvet Harbor logo
First name and last name
Title
Email address
Phone number and type (in whatever order looks best for the design
Website (the website does not need to be in the same block as the personal info)

For example:

Nessa Pryle
Founder & Principal
nessa@velvetharbor.com
+1.628.309.4156 mobile (can use "." or spaces in between blocks of numbers)
velvetharbor.com (somewhere on the card, it does not need to be with the personal info; and note that there is no "www." at the beginning)

Note that there will be no address listed on the business card.

Target Market(s)

Executives (CEO, head of marketing, head of sales) at medical technology and health technology companies, mostly in their 40s and older, well-educated, often with advanced degrees. They are strategic thinkers, responsible for budgets, and familiar with P&L. Their comfort with and trust in using outside consultants varies.

Industry/Entity Type

Medical technology and health technology companies.

Contact Information for Business Card

See project description

Font styles to use
Sans Serif

Requirements
Must have
• Logo and see Business card details section above.

```html
<!DOCTYPE html>
<html lang="en">
<head>
<meta charset="utf-8">
<title>Velvet Harbor — Business Card</title>
<link rel="stylesheet" href="https://fonts.googleapis.com/css2?family=Source+Sans+3:wght@400;600&display=swap">
<style>
  :root {
    --brand-orange: #FF5501;
    --brand-gray: #282B2D;
    --paper: #FFFFFF;
    --card-edge: #3a3d40;
  }
  * { box-sizing: border-box; margin: 0; padding: 0; }
  html, body {
    width: 1200px; height: 1200px; overflow: hidden;
    background: var(--paper);
    font-family: "Source Sans 3", "Myriad Pro", sans-serif;
  }
  .canvas { position: relative; width: 1200px; height: 1200px; }

  .card {
    position: absolute; left: 167px; width: 841px; height: 480px; overflow: hidden;
  }
  .card--front { top: 120px; background: var(--paper); border: 1px solid var(--card-edge); }
  .card--back { top: 622px; background: var(--brand-orange); }

  .person { position: absolute; left: 48px; top: 88px; color: var(--brand-gray); }
  .person__name { font-size: 50px; font-weight: 400; line-height: 1; letter-spacing: -0.5px; text-transform: uppercase; }
  .person__title { font-size: 19px; margin-top: 8px; }

  .contact-bar {
    position: absolute; left: 43px; top: 330px; bottom: 0; width: 29px;
    background: var(--brand-orange);
  }
  .contact-list { position: absolute; left: 43px; top: 333px; list-style: none; }
  .contact-list__item {
    display: flex; align-items: center; height: 29.5px;
    font-size: 20px; color: var(--brand-gray);
  }
  .contact-list__icon { width: 29px; display: flex; justify-content: center; }
  .contact-list__icon svg { width: 13px; height: 13px; fill: none; stroke: var(--paper); stroke-width: 1.6; }
  .contact-list__text { margin-left: 10px; }

  .brand-front {
    position: absolute; right: 70px; top: 200px;
    display: flex; align-items: center; gap: 16px;
    color: var(--brand-gray); font-size: 40px; font-weight: 600;
  }
  .brand-front__dot { width: 30px; height: 30px; border-radius: 50%; background: var(--brand-orange); }

  .brand-back {
    position: absolute; left: 0; right: 0; top: 0; bottom: 0;
    display: flex; align-items: center; justify-content: center; gap: 22px;
    color: var(--paper);
  }
  .brand-back__dot { width: 26px; height: 26px; border-radius: 50%; background: var(--paper); }
  .brand-back__name {
    font-size: 38px; font-weight: 600; line-height: 1.02;
    letter-spacing: 10px; text-transform: uppercase;
  }
</style>
</head>
<body>
<main class="canvas">
  <section class="card card--front" aria-label="Card front">
    <div class="person">
      <h1 class="person__name">Nessa Pryle</h1>
      <p class="person__title">Founder &amp; Principal</p>
    </div>

    <div class="contact-bar"></div>
    <ul class="contact-list">
      <li class="contact-list__item">
        <span class="contact-list__icon"><svg viewBox="0 0 16 16"><path d="M3 1.5l3 3-1.5 2a8 8 0 0 0 5 5l2-1.5 3 3-2 2C7 14 2 9 1 3.5z" fill="#fff" stroke="none"/></svg></span>
        <span class="contact-list__text">+1.628.309.4156</span>
      </li>
      <li class="contact-list__item">
        <span class="contact-list__icon"><svg viewBox="0 0 16 16"><rect x="1" y="3" width="14" height="10"/><path d="M1 3l7 6 7-6M1 13l5-5M15 13l-5-5"/></svg></span>
        <span class="contact-list__text">nessa@velvetharbor.com</span>
      </li>
      <li class="contact-list__item">
        <span class="contact-list__icon"><svg viewBox="0 0 16 16"><circle cx="8" cy="8" r="6.5"/><ellipse cx="8" cy="8" rx="3" ry="6.5"/><path d="M1.5 8h13M2.5 4.8h11M2.5 11.2h11"/></svg></span>
        <span class="contact-list__text">velvetharbor.com</span>
      </li>
    </ul>

    <div class="brand-front">
      <span class="brand-front__dot"></span>
      <span class="brand-front__name">Velvet Harbor</span>
    </div>
  </section>

  <section class="card card--back" aria-label="Card back">
    <div class="brand-back">
      <span class="brand-back__dot"></span>
      <span class="brand-back__name">Velvet<br>Harbor</span>
    </div>
  </section>
</main>
</body>
</html>
```